Business Card Design needed for start up company Pramora

In need of a new business card designed for a start up company based in Sydney, Pramora is a new start up innovative Company, our mission it to make property accessible for everyday Australian and to become the leading Real Estate platform in Australia. We want it to be fresh and clean.

Industry/Entity Type

Financial

Contact Information for Business Card

Section for Name
Section for Title

PRAMORA - Where Doors Open Wide
Mobile:
Direct:

Font styles to use
Sans Serif

Colors
33a6d7
0692cd
0255a3
ffffff

Requirements
Must have
• Logo, all business card details

```html
<!DOCTYPE html>
<html lang="en">
<head>
<meta charset="utf-8">
<title>Pramora Business Card</title>
<link href="https://fonts.googleapis.com/css2?family=Roboto:wght@400;700&display=swap" rel="stylesheet">
<style>
  :root {
    --page-bg: #d3d3d3;
    --card-light-top: #ffffff;
    --card-light-bottom: #d6d6d6;
    --brand-sky: #33a6d7;
    --brand-blue: #1c4f95;
    --brand-navy: #1e4678;
    --brand-navy-deep: #1a3962;
    --panel-grey: #4a4a4d;
    --text-white: #ffffff;
    --text-soft: #e6e6e6;
    --text-navy: #1d3f73;
  }
  * { margin: 0; padding: 0; box-sizing: border-box; }
  html, body { width: 1200px; height: 965px; overflow: hidden; }
  body {
    background: var(--page-bg);
    font-family: "Roboto", Arial, sans-serif;
    position: relative;
  }
  .card {
    position: absolute;
    left: 277px;
    width: 648px;
    border-radius: 40px;
    overflow: hidden;
  }
  .card-front {
    top: 97px;
    height: 368px;
    background: linear-gradient(to bottom, var(--card-light-top) 0%, #eeeeee 55%, var(--card-light-bottom) 100%);
  }
  .card-back {
    top: 502px;
    height: 370px;
    background: linear-gradient(to bottom, var(--brand-navy) 0%, var(--brand-navy-deep) 100%);
  }
  .card-shapes { position: absolute; inset: 0; }
  .brand {
    position: absolute;
    display: flex;
    align-items: center;
    font-weight: 700;
    line-height: 1;
    white-space: nowrap;
  }
  .brand-dot { border-radius: 50%; flex: none; }
  .front-brand { left: 46px; top: 50px; color: var(--brand-navy); font-size: 43px; gap: 6px; }
  .front-brand .brand-dot { width: 92px; height: 92px; background: var(--brand-sky); }
  .back-brand { left: 89px; top: 115px; color: var(--text-white); font-size: 64px; gap: 12px; }
  .back-brand .brand-dot { width: 142px; height: 142px; background: var(--text-white); }
  .person { position: absolute; left: 49px; top: 216px; color: var(--text-white); }
  .person-name { font-size: 21px; font-weight: 700; line-height: 1.2; }
  .person-title { font-size: 15px; line-height: 1.2; }
  .front-web { position: absolute; left: 49px; top: 302px; font-size: 14px; color: var(--text-navy); }
  .contact-list { position: absolute; left: 384px; top: 181px; list-style: none; color: var(--text-soft); font-size: 14.5px; }
  .contact-list li { display: flex; align-items: center; height: 19px; gap: 7px; }
  .contact-list svg { width: 15px; height: 13px; fill: var(--text-soft); }
  .address { position: absolute; left: 383px; top: 250px; color: var(--text-soft); font-size: 14.5px; line-height: 19px; }
  .back-web {
    position: absolute; left: 0; right: 0; top: 331px;
    text-align: center; color: var(--text-soft);
    font-size: 14px; letter-spacing: 5px;
  }
</style>
</head>
<body>
  <section class="card card-front">
    <svg class="card-shapes" width="648" height="368" viewBox="0 0 648 368">
      <polygon points="341,169 648,169 648,305 281,305" fill="var(--panel-grey)"/>
      <polygon points="0,200 351,200 319,277 0,277" fill="var(--brand-blue)"/>
      <polyline points="351,200 319,277" stroke="#ffffff" stroke-width="5" fill="none"/>
    </svg>
    <div class="brand front-brand"><span class="brand-dot"></span><span class="brand-name">PRAMORA</span></div>
    <div class="person">
      <p class="person-name">Liam Carter</p>
      <p class="person-title">Managing Director</p>
    </div>
    <p class="front-web">www.pramora.com</p>
    <ul class="contact-list">
      <li><svg viewBox="0 0 15 13"><rect x="1" y="1" width="4" height="11"/><rect x="6" y="2" width="8" height="10"/></svg>+61 2 9000 4120</li>
      <li><svg viewBox="0 0 15 13"><path d="M2 1 L5 1 L6 4 L4.5 5.5 Q6.5 8.5 9.5 10 L11 8.5 L14 9.5 L14 12 Q6 13 2 1 Z"/></svg>+61 400 318 752</li>
      <li><svg viewBox="0 0 15 13"><path d="M1 2 H14 V11 H1 Z M1 2 L7.5 7.5 L14 2" fill="none" stroke="#e6e6e6" stroke-width="1.5"/></svg>info@pramora.com</li>
    </ul>
    <p class="address">Here your company or<br>home address</p>
  </section>

  <section class="card card-back">
    <div class="brand back-brand"><span class="brand-dot"></span><span class="brand-name">PRAMORA</span></div>
    <p class="back-web">www.pramora.com</p>
  </section>
</body>
</html>
```